New Product/Company Launch Postcard Design

I need a postcard design for a new product launch/new company called Trinvelas. Trinvelas are decorative ring hooks designed to decorate home fixtures for holidays, seasons and special occasions. The rings have hooks for hanging your favorite hanging ornaments, party decorations or fashionable accessories. Trinvelas comes in 3 sizes; small, medium and large with 4 available colors to accommodate most home fixtures. The rings have a split opening for easy attaching or placing on home fixtures, so there are no tools, no glue, the ring is easily attachable. The rings are simply easy to decorate and easy to create ideas.

I would like the postcard to communicate the product use and would like it to drive customers to my website. On this postcard, I am offering $4.99 2-pack special, Introductory offer. I would also like the postcard to direct them to my website to sign up for specials and offers, by doing so, I will give away a free small Trinvela. Please visit my website at www.trinvelasdesigns.com for other creative ideas.

I had someone create the logo, the colors I chose were black, hot pink and yellow. However, if the logo doesn't seem to work on the design, I am open for comments or other ideas.

```html
<!DOCTYPE html>
<html lang="en">
<head>
<meta charset="utf-8">
<title>Trinvelas – Launch Postcard</title>
<link rel="stylesheet" href="https://fonts.googleapis.com/css2?family=Tinos:ital@0;1&family=Oswald:wght@400;600&family=Krona+One&family=Open+Sans:wght@400;700&display=swap">
<style>
  :root {
    --black: #000000;
    --hot-pink: #ff1aa6;
    --yellow: #f5bb0a;
    --logo-yellow: #f4f000;
    --white: #ffffff;
    --ink: #111111;
    --star-shadow: #5a5a5a;
  }
  * { margin: 0; padding: 0; box-sizing: border-box; }
  html, body { width: 1200px; height: 1000px; overflow: hidden; background: var(--white); }
  .postcard { position: relative; width: 1200px; height: 1000px; overflow: hidden; background: var(--yellow); }

  .top-band { position: absolute; left: 0; top: 0; width: 1200px; height: 455px; background: var(--black); }

  .brand-name {
    position: absolute; left: 40px; top: 70px; width: 520px; text-align: center;
    font-family: "Oswald", sans-serif; font-weight: 400; font-size: 130px; line-height: 1;
    color: var(--logo-yellow);
  }

  .tagline {
    position: absolute; left: 520px; top: 14px; width: 680px; text-align: center;
    font-family: "Tinos", serif; font-style: italic; font-size: 31px; line-height: 52px;
    color: var(--white); letter-spacing: 0.5px;
  }

  .price-burst { position: absolute; left: 760px; top: 120px; width: 440px; height: 350px; }
  .price-text {
    position: absolute; left: 790px; top: 190px; width: 380px; text-align: center;
    font-family: "Open Sans", sans-serif; color: var(--ink);
  }
  .price-amount { font-size: 78px; line-height: 84px; }
  .price-pack { font-size: 34px; line-height: 36px; }
  .price-sizes { font-size: 23px; font-weight: 700; line-height: 50px; }

  .shipping-headline {
    position: absolute; left: 0; top: 468px; width: 1200px; text-align: center;
    font-family: "Krona One", sans-serif; font-size: 40px; line-height: 50px;
    color: var(--ink); letter-spacing: 2px;
  }
  .offer-line {
    position: absolute; left: 0; top: 518px; width: 1200px; text-align: center;
    font-family: "Krona One", sans-serif; font-size: 23px; line-height: 32px;
    color: var(--ink); letter-spacing: 2px; padding-left: 20px;
  }

  .use-label {
    position: absolute; font-family: "Tinos", serif; font-size: 30px; line-height: 38px;
    color: var(--ink); text-align: center;
  }
  .use-photo { position: absolute; }
  .photo-pendant { left: 50px; top: 644px; width: 193px; height: 187px; background: radial-gradient(circle at 50% 55%, #f4b040, #c24a12 55%, #3a1a10); }
  .photo-vases { left: 274px; top: 647px; width: 146px; height: 184px; background: linear-gradient(180deg, #5a2a14, #8a4a26 60%, #3b1a0c); }
  .photo-mantels { left: 500px; top: 643px; width: 193px; height: 188px; background: linear-gradient(135deg, #c9a26c, #7a5230 60%, #3a2416); }
  .photo-bedrooms { left: 720px; top: 648px; width: 190px; height: 182px; background: linear-gradient(180deg, #f3f3f0, #b9c6cf 55%, #4c5a66); }
  .photo-lamps { left: 962px; top: 648px; width: 184px; height: 178px; background: linear-gradient(160deg, #2b2622, #6a5a48 55%, #d9c8a8); }

  .cta-arrow { position: absolute; left: 0; top: 836px; width: 1200px; height: 164px; }
  .cta-text {
    position: absolute; left: 18px; top: 889px;
    font-family: "Oswald", sans-serif; font-weight: 600; font-size: 37px; line-height: 52px;
    color: var(--ink); letter-spacing: 0.3px;
  }
</style>
</head>
<body>
<main class="postcard">
  <section class="top-band">
    <div class="brand-name">Trinvelas</div>

    <p class="tagline">A "NEW" SIMPLE SOLUTION HOOK<br>FOR HANGING DECORATIVE ACCESSORIES</p>

    <svg class="price-burst" viewBox="0 0 440 350" aria-hidden="true">
      <g transform="translate(212,168) scale(1.18,1)">
        <polygon fill="var(--star-shadow)" points="165,0 132.4,26.3 152.5,63.2 112.2,75.1 116.7,116.7 75.1,112.2 63.2,152.5 26.3,132.4 0,165 -26.3,132.4 -63.2,152.5 -75.1,112.2 -116.7,116.7 -112.2,75.1 -152.5,63.2 -132.4,26.3 -165,0 -132.4,-26.3 -152.5,-63.2 -112.2,-75.1 -116.7,-116.7 -75.1,-112.2 -63.2,-152.5 -26.3,-132.4 0,-165 26.3,-132.4 63.2,-152.5 75.1,-112.2 116.7,-116.7 112.2,-75.1 152.5,-63.2 132.4,-26.3"/>
      </g>
      <g transform="translate(224,178) scale(1.15,0.98)">
        <polygon fill="var(--white)" stroke="var(--hot-pink)" stroke-width="5" points="165,0 132.4,26.3 152.5,63.2 112.2,75.1 116.7,116.7 75.1,112.2 63.2,152.5 26.3,132.4 0,165 -26.3,132.4 -63.2,152.5 -75.1,112.2 -116.7,116.7 -112.2,75.1 -152.5,63.2 -132.4,26.3 -165,0 -132.4,-26.3 -152.5,-63.2 -112.2,-75.1 -116.7,-116.7 -75.1,-112.2 -63.2,-152.5 -26.3,-132.4 0,-165 26.3,-132.4 63.2,-152.5 75.1,-112.2 116.7,-116.7 112.2,-75.1 152.5,-63.2 132.4,-26.3"/>
      </g>
    </svg>
    <div class="price-text">
      <div class="price-amount">$4.99</div>
      <div class="price-pack">2 Pack</div>
      <div class="price-sizes">Small, Medium, Large</div>
    </div>
  </section>

  <h1 class="shipping-headline">FREE SHIPPING ON ALL ORDERS OVER $15</h1>
  <p class="offer-line">INTRODUCTORY OFFER $4.99 FOR 2-PACK</p>

  <div class="use-label" style="left:40px; top:556px; width:212px;">Hanging<br>Pendant Lights</div>
  <div class="use-label" style="left:284px; top:592px; width:126px;">Vases</div>
  <div class="use-label" style="left:500px; top:596px; width:193px;">Mantels</div>
  <div class="use-label" style="left:712px; top:594px; width:190px;">Bedrooms</div>
  <div class="use-label" style="left:950px; top:596px; width:192px;">Table Lamps</div>

  <div class="use-photo photo-pendant" role="img" aria-label="Photo of a glowing glass pendant light decorated with a ring hook"></div>
  <div class="use-photo photo-vases" role="img" aria-label="Photo of a decorative vase in a wooden cabinet with a ring hook and charms"></div>
  <div class="use-photo photo-mantels" role="img" aria-label="Photo of a stone fireplace mantel with a candle holder decorated by a ring hook"></div>
  <div class="use-photo photo-bedrooms" role="img" aria-label="Photo of a bedside table lamp with a ring hook detail inset"></div>
  <div class="use-photo photo-lamps" role="img" aria-label="Photo of a table lamp with hanging crystal ring hook accessories and close-up insets"></div>

  <svg class="cta-arrow" viewBox="0 0 1200 164" aria-hidden="true">
    <polygon fill="var(--hot-pink)" points="0,44 628,44 628,0 1200,82 628,164 628,120 0,120"/>
  </svg>
  <p class="cta-text">Please visit my website at www.trinvelasdesigns.com</p>
</main>
</body>
</html>
```